Home care agency

Current website QTRBLOOMS.com. Need to update and reformat to different pages. use my info from my current website

Target Market(s)

adult children

Industry/Entity Type

Home Health

Coding

Coded - Design and coding required

Number of Pages Required

4 page

Font styles to use
Sans Serif

Colors
3276b5
33a6d7
3277b5
85cae6
85acd3

```html
<!DOCTYPE html>
<html lang="en">
<head>
<meta charset="utf-8">
<title>Quarter Blooms Home Care</title>
<link rel="stylesheet" href="https://fonts.googleapis.com/css2?family=Roboto:wght@400;500;700;900&family=Open+Sans:wght@400;600&display=swap">
<style>
:root{
  --blue:#3276b5;
  --sky:#33a6d7;
  --pale:#85cae6;
  --mist:#85acd3;
  --teal:#0f7d8c;
  --teal-dark:#0b6672;
  --ink:#1f2a33;
  --body:#5b6670;
  --wash:#eef6f8;
  --white:#ffffff;
}
*{box-sizing:border-box;margin:0;padding:0}
html,body{width:1200px;height:3748px;overflow:hidden;background:var(--white)}
body{font-family:"Open Sans",Arial,sans-serif;color:var(--body);position:relative}
.page{position:relative;width:1200px;height:3748px;overflow:hidden}
.abs{position:absolute}
h1,h2,h3{font-family:"Roboto",Arial,sans-serif;color:var(--ink)}
.btn{position:absolute;display:flex;align-items:center;justify-content:center;background:var(--teal);color:var(--white);font-family:"Roboto",Arial,sans-serif;font-weight:700;font-size:15px;border-radius:24px;height:44px}

/* header */
.brand{left:160px;top:8px;display:flex;align-items:center;gap:10px}
.brand-mark{width:58px;height:58px;border-radius:50%;border:3px solid var(--teal)}
.brand-name{font-family:"Roboto",Arial,sans-serif;font-weight:700;font-size:14px;color:var(--teal);width:110px;line-height:1.2}
.nav{left:462px;top:36px;display:flex;gap:44px;font-family:"Roboto",Arial,sans-serif;font-size:14px;color:var(--ink)}
.btn-nav{left:936px;top:28px;width:104px;height:36px;font-size:14px}

/* hero */
.hero-title{left:160px;top:214px;font-size:36px;font-weight:900;line-height:1.15;white-space:nowrap}
.hero-text{left:160px;top:326px;width:330px;font-size:13px;line-height:1.6}
.btn-hero{left:160px;top:424px;width:232px}
.hero-art{left:660px;top:70px;width:420px;height:440px;border-radius:46% 54% 50% 50%;background:radial-gradient(circle at 45% 40%,#e7f4f8 0%,#cfe8f0 55%,#ffffff 72%)}

/* about */
.about-band{left:0;top:560px;width:1200px;height:900px}
.about-title{left:0;top:780px;width:1200px;text-align:center;color:var(--white);font-size:40px;font-weight:700}
.about-text{left:290px;top:858px;width:620px;text-align:center;color:var(--white);font-size:13px;line-height:1.7}
.about-art{left:240px;top:1100px;width:720px;height:380px;border-radius:20px;background:linear-gradient(180deg,rgba(255,255,255,.18) 0%,rgba(133,202,230,.35) 100%)}

/* services */
.services-title{left:0;top:1592px;width:1200px;text-align:center;font-size:34px;font-weight:700}
.service-card{top:1680px;width:280px;height:300px;background:var(--white);border-radius:6px;box-shadow:0 4px 18px rgba(30,60,80,.13);padding:26px 24px}
.service-icon{width:42px;height:42px;margin-bottom:14px}
.service-card h3{font-size:16px;font-weight:700;margin-bottom:10px}
.service-card ul{list-style:none;font-size:12px;line-height:1.75}

/* home sweet home */
.hsh-band{left:0;top:2040px;width:1200px;height:800px}
.hsh-title{left:0;top:2222px;width:1200px;text-align:center;font-size:38px;font-weight:700}
.feature-card{width:260px;height:300px;background:var(--white);box-shadow:0 6px 22px rgba(30,60,80,.14);text-align:center;padding:28px 24px}
.feature-icon{width:80px;height:80px;border-radius:50%;background:var(--teal);margin:0 auto 22px;display:flex;align-items:center;justify-content:center}
.feature-card h3{font-size:15px;font-weight:700;margin-bottom:12px}
.feature-card p{font-size:12px;line-height:1.65}
.btn-more{left:544px;top:2760px;width:112px;height:40px;font-size:14px}

/* appointment */
.cta-title{left:0;top:2950px;width:1200px;text-align:center;font-size:34px;font-weight:700}
.cta-text{left:250px;top:3012px;width:700px;text-align:center;font-size:13px;line-height:1.7}
.btn-book{left:454px;top:3120px;width:158px;height:40px;font-size:14px}
.btn-contact{left:628px;top:3120px;width:118px;height:40px;font-size:14px}

/* footer */
.footer-band{left:0;top:3170px;width:1200px;height:578px}
.footer-brand{left:0;top:3290px;width:1200px;display:flex;flex-direction:column;align-items:center;gap:8px}
.footer-brand .brand-mark{border-color:var(--white)}
.footer-brand .brand-name{color:var(--white);text-align:center;width:auto}
.footer-nav{left:0;top:3424px;width:1200px;display:flex;justify-content:center;gap:58px;font-family:"Roboto",Arial,sans-serif;font-size:14px;color:var(--white)}
.footer-rule{left:160px;top:3466px;width:880px;height:1px;background:rgba(255,255,255,.35)}
.contact-item{top:3500px;width:200px;text-align:center;color:var(--white);font-size:12px;line-height:1.5}
.contact-icon{width:48px;height:48px;border-radius:50%;background:var(--white);margin:0 auto 10px;display:flex;align-items:center;justify-content:center}
.social{left:0;top:3628px;width:1200px;display:flex;justify-content:center;gap:12px}
.social span{width:30px;height:30px;border-radius:4px;background:var(--white);opacity:.9}
.legal{left:0;top:3712px;width:1200px;height:36px;background:var(--teal-dark);color:var(--white);font-size:12px;display:flex;align-items:center;justify-content:center}
</style>
</head>
<body>
<div class="page">

  <!-- header -->
  <div class="abs brand"><span class="brand-mark"></span><span class="brand-name">Quarter Blooms Home Care</span></div>
  <nav class="abs nav"><span>Home</span><span>About Us</span><span>Services</span><span>Why Us?</span><span>Contact Us</span></nav>
  <a class="btn btn-nav">Contact Us</a>

  <!-- hero -->
  <h1 class="abs hero-title">Providing Care Throughout<br>the South Shore</h1>
  <p class="abs hero-text">Quarter Blooms Home Care is owned and operated by Dana Whitcomb, a registered nurse who has served the local health care system since 2001.</p>
  <a class="btn btn-hero">Schedule Free Consulting</a>
  <div class="abs hero-art" role="img" aria-label="Illustration of a red first aid kit with pills, a thermometer and a stethoscope"></div>

  <!-- about -->
  <svg class="abs about-band" viewBox="0 0 1200 900" preserveAspectRatio="none" aria-hidden="true">
    <defs>
      <linearGradient id="aboutGrad" x1="0" y1="0" x2="1" y2="1">
        <stop offset="0" stop-color="#33a6d7"/>
        <stop offset="0.55" stop-color="#3276b5"/>
        <stop offset="1" stop-color="#2b5f9a"/>
      </linearGradient>
    </defs>
    <path d="M0 230 C 260 120 620 40 1200 0 L1200 640 C 900 760 560 800 0 820 Z" fill="url(#aboutGrad)"/>
  </svg>
  <h2 class="abs about-title">About Us</h2>
  <p class="abs about-text">Quarter Blooms Home Care is owned and operated by Dana Whitcomb, a registered nurse and lifelong resident of the South Shore who has worked in health care since 2001. We specialize in home care, staffing and respite services, and every caregiver is trained to treat clients like family.<br><br>All of our caregivers have passed background checks and training, and we follow every state guideline. We help families plan care so loved ones can remain safe, comfortable and independent in the homes they know best.</p>
  <div class="abs about-art" role="img" aria-label="Illustration of a doctor at a desk speaking with an elderly patient holding a cane"></div>

  <!-- services -->
  <h2 class="abs services-title">Our Services</h2>
  <div class="abs service-card" style="left:160px">
    <svg class="service-icon" viewBox="0 0 42 42" aria-hidden="true"><rect x="15" y="4" width="12" height="34" rx="2" fill="#0f7d8c"/><rect x="4" y="15" width="34" height="12" rx="2" fill="#0f7d8c"/></svg>
    <h3>Skilled Care Services</h3>
    <ul><li>Skilled Nursing Assessments</li><li>Medication Management</li><li>Wound Care</li><li>Injections</li><li>Medical Case Assistance</li><li>Transportation to Medical Appointments</li><li>Care Plan Management</li></ul>
  </div>
  <div class="abs service-card" style="left:460px">
    <svg class="service-icon" viewBox="0 0 42 42" aria-hidden="true"><circle cx="21" cy="21" r="18" fill="none" stroke="#0f7d8c" stroke-width="4"/><path d="M13 22 l6 6 l11 -13" fill="none" stroke="#0f7d8c" stroke-width="4"/></svg>
    <h3>Non-Medical Services</h3>
    <ul><li>Live-In Care</li><li>Respite Care</li><li>Assisting with Daily Living Activities</li><li>Meal Preparation</li><li>Companionship</li><li>Homemaking</li></ul>
  </div>
  <div class="abs service-card" style="left:760px">
    <svg class="service-icon" viewBox="0 0 42 42" aria-hidden="true"><path d="M8 24 a13 13 0 0 1 26 0" fill="none" stroke="#0f7d8c" stroke-width="4"/><rect x="5" y="22" width="8" height="12" rx="3" fill="#0f7d8c"/><rect x="29" y="22" width="8" height="12" rx="3" fill="#0f7d8c"/></svg>
    <h3>Client Benefits</h3>
    <ul><li>Continuity of care with one caregiver</li><li>Care visits on a regular basis</li><li>Open communication with nurses by phone or email</li><li>Ongoing reviews for the client's family</li><li>No long-term contracts required</li><li>Streamlined payment process</li></ul>
  </div>

  <!-- home sweet home -->
  <svg class="abs hsh-band" viewBox="0 0 1200 800" preserveAspectRatio="none" aria-hidden="true">
    <path d="M0 60 C 360 -20 760 -10 1200 70 L1200 720 C 820 800 380 790 0 720 Z" fill="#eef6f8"/>
  </svg>
  <h2 class="abs hsh-title">Quarter Blooms</h2>
  <div class="abs feature-card" style="left:208px;top:2320px">
    <div class="feature-icon"><svg width="40" height="40" viewBox="0 0 40 40" aria-hidden="true"><path d="M6 20 L20 8 L34 20 V34 H6 Z" fill="none" stroke="#fff" stroke-width="3"/></svg></div>
    <h3>Why Choose Home Care?</h3>
    <p>Home care is a cost-effective option that allows clients to recover and stay independent in the comfort of their own home.</p>
  </div>
  <div class="abs feature-card" style="left:470px;top:2400px">
    <div class="feature-icon"><svg width="40" height="40" viewBox="0 0 40 40" aria-hidden="true"><circle cx="20" cy="20" r="14" fill="none" stroke="#fff" stroke-width="3"/><path d="M20 11 V20 L26 24" fill="none" stroke="#fff" stroke-width="3"/></svg></div>
    <h3>Care Schedule/Frequency</h3>
    <p>Home care hours are flexible and based on your needs. There are no weekly minimums for medical or non-medical care.</p>
  </div>
  <div class="abs feature-card" style="left:742px;top:2480px">
    <div class="feature-icon"><svg width="40" height="40" viewBox="0 0 40 40" aria-hidden="true"><rect x="6" y="11" width="28" height="19" rx="3" fill="none" stroke="#fff" stroke-width="3"/><path d="M6 17 H34" stroke="#fff" stroke-width="3"/></svg></div>
    <h3>Payment Options</h3>
    <p>Quarter Blooms currently accepts private pay and long-term care insurance payment plans.</p>
  </div>
  <a class="btn btn-more">Read More</a>

  <!-- appointment -->
  <h2 class="abs cta-title">Ready To Get Appointment?</h2>
  <p class="abs cta-text">Thank you for considering Quarter Blooms for your needs. Information about your medical conditions, care and financial situation lets us recommend a plan so all parties can make decisions with confidence.</p>
  <a class="btn btn-book">Book Appointment</a>
  <a class="btn btn-contact">Contact Us</a>

  <!-- footer -->
  <svg class="abs footer-band" viewBox="0 0 1200 578" preserveAspectRatio="none" aria-hidden="true">
    <path d="M0 40 C 360 -10 760 0 1200 90 L1200 578 L0 578 Z" fill="#85cae6" opacity=".45"/>
    <path d="M0 90 C 400 20 800 30 1200 120 L1200 578 L0 578 Z" fill="#0f7d8c"/>
  </svg>
  <div class="abs footer-brand"><span class="brand-mark"></span><span class="brand-name">Quarter Blooms Home Care</span></div>
  <nav class="abs footer-nav"><span>Home</span><span>About Us</span><span>Services</span><span>Why Us?</span><span>Contact Us</span></nav>
  <div class="abs footer-rule"></div>
  <div class="abs contact-item" style="left:340px">
    <div class="contact-icon"><svg width="22" height="22" viewBox="0 0 24 24" aria-hidden="true"><path d="M12 2 C7 2 4 6 4 10 C4 16 12 22 12 22 C12 22 20 16 20 10 C20 6 17 2 12 2 Z" fill="#0f7d8c"/><circle cx="12" cy="10" r="3" fill="#fff"/></svg></div>
    12 Harbor Rd<br>Marshfield MA
  </div>
  <div class="abs contact-item" style="left:500px">
    <div class="contact-icon"><svg width="22" height="22" viewBox="0 0 24 24" aria-hidden="true"><path d="M5 3 L9 3 L11 8 L8.5 10 C9.5 12.5 11.5 14.5 14 15.5 L16 13 L21 15 L21 19 C21 20 20 21 19 21 C10 21 3 14 3 5 C3 4 4 3 5 3 Z" fill="#0f7d8c"/></svg></div>
    Call us on<br>(781) 555-0142
  </div>
  <div class="abs contact-item" style="left:660px">
    <div class="contact-icon"><svg width="22" height="22" viewBox="0 0 24 24" aria-hidden="true"><rect x="3" y="5" width="18" height="14" rx="2" fill="#0f7d8c"/><path d="M3 6 L12 13 L21 6" fill="none" stroke="#fff" stroke-width="2"/></svg></div>
    Email<br>info@qtrblooms.com
  </div>
  <div class="abs social"><span></span><span></span><span></span><span></span></div>
  <div class="abs legal">Copyright © 2019 Quarter Blooms Home Care. Terms &amp; Conditions | Privacy Policy</div>

</div>
</body>
</html>
```